Business Stationery Design

I would like to get some stationery designed for my company. The stationery should include a letterhead, envelope, and business card. We are a technology consulting company specializing in Healthcare IT, and Education management systems. The colors of the stationery should match the logo. The logo is uploaded.

Target Market(s)

Hospitals, Clinics. Doctors offices. Private Schools.

Industry/Entity Type

Business

```html
<!DOCTYPE html>
<html lang="en">
<head>
<meta charset="utf-8">
<title>Larkspur Advisory Group — Stationery</title>
<link href="https://fonts.googleapis.com/css2?family=Open+Sans:wght@400;600&family=Montserrat:wght@500&display=swap" rel="stylesheet">
<style>
  :root{
    --green:#78be34;
    --yellow:#f5b800;
    --white:#ffffff;
    --ink:#3c3c3c;
    --muted:#6d6d6d;
    --backdrop:#ebe7e1;
    --shadow:0 6px 14px rgba(0,0,0,.18);
  }
  *{box-sizing:border-box;margin:0;padding:0}
  html,body{width:1200px;height:1200px;overflow:hidden}
  body{background:var(--backdrop);font-family:"Open Sans",Arial,sans-serif;position:relative}
  .sheet{position:absolute;background:var(--white);box-shadow:var(--shadow);overflow:hidden}
  .sheet svg.art{position:absolute;inset:0;width:100%;height:100%}

  /* brand name stand-in */
  .mark{position:absolute;display:flex;align-items:center;gap:6px;font-family:"Open Sans",Arial,sans-serif;font-weight:600;color:var(--green);white-space:nowrap}
  .mark .dot{border-radius:50%;background:currentColor;flex:none}

  /* folder */
  .folder{left:88px;top:56px;width:476px;height:672px;background:var(--green)}
  .folder .mark{color:var(--white);left:50%;top:330px;transform:translateX(-50%);font-size:30px;gap:12px}
  .folder .mark .dot{width:22px;height:22px}

  /* letterhead */
  .letterhead{left:651px;top:56px;width:475px;height:673px}
  .letterhead .mark{left:44px;top:118px;font-size:13px}
  .letterhead .mark .dot{width:10px;height:10px}
  .letter-body{position:absolute;left:50px;top:198px;width:377px;font-size:9.6px;line-height:13.7px;color:var(--ink);text-align:justify}
  .letter-body p{margin-bottom:13.7px}
  .signature{position:absolute;left:50px;top:550px;font-size:9.6px;color:var(--ink)}
  .signature-line{position:absolute;left:50px;top:600px;width:60px;border-top:1px solid var(--ink)}
  .contact{position:absolute;list-style:none;text-align:right;color:var(--ink)}
  .contact li{display:flex;justify-content:flex-end;align-items:center}
  .contact svg{fill:var(--green);flex:none}
  .letterhead .contact{right:30px;top:589px;font-size:7.6px}
  .letterhead .contact li{height:17.5px;gap:10px}
  .letterhead .contact svg{width:10px;height:10px}

  /* envelope */
  .envelope-back{left:89px;top:758px;width:477px;height:191px}
  .envelope-front{left:89px;top:980px;width:477px;height:193px}
  .envelope-front .mark{left:34px;top:70px;font-size:12px}
  .envelope-front .mark .dot{width:9px;height:9px}
  .envelope-front .band{position:absolute;left:0;right:0;bottom:0;height:17px;background:var(--green)}

  /* business cards */
  .card-front{left:745px;top:807px;width:274px;height:157px}
  .card-front .mark{left:22px;top:84px;font-size:10px;gap:4px}
  .card-front .mark .dot{width:8px;height:8px}
  .person{position:absolute;right:25px;top:28px;text-align:right}
  .person .name{font-family:"Montserrat",Arial,sans-serif;font-weight:500;font-size:16px;letter-spacing:1.5px;color:var(--muted);line-height:18px}
  .person .title{font-size:5.5px;letter-spacing:5px;color:var(--yellow);margin-right:-5px}
  .card-front .contact{right:38px;top:86px;font-size:6.5px;color:var(--muted)}
  .card-front .contact li{height:13.3px;gap:8px}
  .card-front .contact svg{width:7px;height:7px}

  .card-back{left:746px;top:985px;width:274px;height:157px}
  .card-back .mark{left:50%;top:50px;transform:translateX(-50%);font-size:13px}
  .card-back .mark .dot{width:10px;height:10px}
</style>
</head>
<body>

<section class="sheet folder" aria-label="Presentation folder">
  <svg class="art" viewBox="0 0 476 672" preserveAspectRatio="none">
    <path fill="var(--white)" d="M0,640 Q330,618 476,500 L476,672 L0,672Z"/>
    <path fill="var(--green)" d="M0,648 Q340,632 476,535 L476,672 L0,672Z"/>
    <path fill="var(--yellow)" d="M0,656 Q340,648 476,572 L476,672 L0,672Z"/>
  </svg>
  <div class="mark"><span class="dot"></span>Larkspur Advisory</div>
</section>

<section class="sheet letterhead" aria-label="Letterhead">
  <svg class="art" viewBox="0 0 475 673" preserveAspectRatio="none">
    <path fill="var(--yellow)" d="M0,0 H475 V10 Q220,20 0,95Z"/>
    <path fill="var(--green)" d="M0,118 Q40,85 140,66 Q260,36 475,22 L475,28 Q230,45 150,85 Q60,130 0,190Z"/>
    <circle cx="80" cy="118" r="46" fill="var(--white)"/>
  </svg>
  <div class="mark"><span class="dot"></span>Larkspur Advisory</div>
  <div class="letter-body">
    <p>Solum nullam principes vis no, eleifend postulant mediocrem ut est, ad tota partem quo. Vix lorem putant scribentur no, mea meis solet melius no, pri feugait noluisse appetere no. Ei mea graece suscipit, fastidii probatus est et. Duo ut opor&shy;tere iudicabit, exerci laoreet vim id. An vidit quidam cum, ceteros phaedrum sit ea. Mollis incorrupte in vix. Noster mnesarchum vix ei</p>
    <p>Ius te maluisset voluptatum quaerendum, no discere saperet persequeris cum, no pro nonumy partem phaedrum. Mel mazim corpora te. Has ad aeque mucius impetus, vel tation regione appetere ne. Porro voluptatum ius ut, ei docendi elo&shy;quentiam sea. Ne mandamus dignissim efficiendi eum, est id tota insolens, eu per facete latine.</p>
    <p>Solum nullam principes vis no, eleifend postulant mediocrem ut est, ad tota partem quo. Vix lorem putant scribentur no, mea meis solet melius no, pri feugait noluisse appetere no. Ei mea graece suscipit, fastidii probatus est et. Duo ut opor&shy;tere iudicabit, exerci laoreet vim id. An vidit quidam cum, ceteros phaedrum sit ea. Mollis incorrupte in vix. Noster mnesarchum vix ei.</p>
    <p>Ius te maluisset voluptatum quaerendum, no discere saperet persequeris cum, no pro nonumy partem phaedrum. Mel mazim corpora te. Has ad aeque mucius impetus, vel tation regione appetere ne. Porro voluptatum ius ut, ei docendi elo&shy;quentiam sea. Ne mandamus dignissim efficiendi eum, est id tota insolens, eu per facete latine.</p>
  </div>
  <div class="signature">Signature</div>
  <div class="signature-line"></div>
  <ul class="contact">
    <li>0123 Zip, ABC City, USA <svg viewBox="0 0 10 10"><path d="M5 0a3.5 3.5 0 0 0-3.5 3.5C1.5 6 5 10 5 10s3.5-4 3.5-6.5A3.5 3.5 0 0 0 5 0zm0 5a1.4 1.4 0 1 1 0-2.8A1.4 1.4 0 0 1 5 5z"/></svg></li>
    <li>+00 1234 56 789 <svg viewBox="0 0 10 10"><path d="M2 0l2 2.4-1 1.3a6 6 0 0 0 3.3 3.3l1.3-1L10 8 8.6 10C4 9.6.4 6 0 1.4z"/></svg></li>
    <li>info@company.com <svg viewBox="0 0 10 10"><path d="M0 2h10v6H0zM0 2l5 3.5L10 2" stroke="#fff" stroke-width=".8"/></svg></li>
    <li>www.company.com <svg viewBox="0 0 10 10"><circle cx="5" cy="5" r="5"/><path d="M0 5h10M5 0c-2.5 3-2.5 7 0 10M5 0c2.5 3 2.5 7 0 10" stroke="#fff" stroke-width=".7" fill="none"/></svg></li>
  </ul>
</section>

<section class="sheet envelope-back" aria-label="Envelope back">
  <svg class="art" viewBox="0 0 477 191" preserveAspectRatio="none">
    <path fill="#ececec" d="M0,0 L238,122 L477,0Z"/>
    <path fill="var(--green)" d="M0,0 H477 L248,112 Q238,117 228,112Z"/>
  </svg>
</section>

<section class="sheet envelope-front" aria-label="Envelope front">
  <div class="mark"><span class="dot"></span>Larkspur Advisory</div>
  <div class="band"></div>
</section>

<section class="sheet card-front" aria-label="Business card front">
  <div class="mark"><span class="dot"></span>Larkspur Advisory</div>
  <div class="person">
    <div class="name">YOUR NAME</div>
    <div class="title">YOUR TITLE</div>
  </div>
  <ul class="contact">
    <li>0123 Zip, ABC City, USA <svg viewBox="0 0 10 10"><path d="M5 0a3.5 3.5 0 0 0-3.5 3.5C1.5 6 5 10 5 10s3.5-4 3.5-6.5A3.5 3.5 0 0 0 5 0zm0 5a1.4 1.4 0 1 1 0-2.8A1.4 1.4 0 0 1 5 5z"/></svg></li>
    <li>+00 1234 56 789 <svg viewBox="0 0 10 10"><path d="M2 0l2 2.4-1 1.3a6 6 0 0 0 3.3 3.3l1.3-1L10 8 8.6 10C4 9.6.4 6 0 1.4z"/></svg></li>
    <li>info@company.com <svg viewBox="0 0 10 10"><path d="M0 2h10v6H0zM0 2l5 3.5L10 2" stroke="#fff" stroke-width=".8"/></svg></li>
    <li>www.company.com <svg viewBox="0 0 10 10"><circle cx="5" cy="5" r="5"/><path d="M0 5h10M5 0c-2.5 3-2.5 7 0 10M5 0c2.5 3 2.5 7 0 10" stroke="#fff" stroke-width=".7" fill="none"/></svg></li>
  </ul>
</section>

<section class="sheet card-back" aria-label="Business card back">
  <svg class="art" viewBox="0 0 274 157" preserveAspectRatio="none">
    <path fill="var(--green)" d="M0,157 Q190,150 274,95 L274,157Z"/>
    <path fill="var(--white)" d="M0,157 Q200,152 274,110 L274,157Z"/>
    <path fill="var(--yellow)" d="M0,157 Q205,154 274,122 L274,157Z"/>
  </svg>
  <div class="mark"><span class="dot"></span>Larkspur Advisory</div>
</section>

</body>
</html>
```